Pelvoran Exploration and Production

We need a powerpoint design for a new exploration company. I would like to either use black logo or change color to a cardinal color. We explore oil and gas exploration. We would like to see designs with a cardinal color. The ppt would be a universal ppt used for presenting deals.

```html
<!DOCTYPE html>
<html lang="en">
<head>
<meta charset="utf-8">
<title>Pelvoran Exploration and Production – Deal Presentation</title>
<link href="https://fonts.googleapis.com/css2?family=Arimo:wght@400;700&display=swap" rel="stylesheet">
<style>
  :root{
    --stage:#dfe5e7;
    --paper:#ffffff;
    --ink:#111111;
    --ink-soft:#4a4a4a;
    --rule:#1a1a1a;
    --ghost:#e6e6e6;
    --ghost-dark:#595959;
    --mark:#141414;
  }
  *{box-sizing:border-box;margin:0;padding:0}
  html,body{width:1200px;height:800px;overflow:hidden}
  body{background:var(--stage);font-family:"Arimo",Arial,sans-serif;color:var(--ink);position:relative}

  .slide{position:absolute;background:var(--paper);overflow:hidden;box-shadow:0 14px 30px rgba(0,0,0,.12)}
  .slide--title{left:290px;top:36px;width:620px;height:349px}
  .slide--content{top:430px;width:540px;height:304px}
  .slide--site{left:45px}
  .slide--facility{left:615px}

  .photo{position:absolute}
  .mark{position:absolute;border-radius:50%;background:var(--mark);color:#fff;display:flex;align-items:center;justify-content:center;font-weight:700;letter-spacing:.04em}

  /* title slide */
  .title__rule-top{position:absolute;left:24px;top:30px;width:140px;height:2px;background:var(--rule)}
  .title__photo{left:190px;top:0;width:430px;height:349px;background:linear-gradient(180deg,#4f7fc4 0%,#6d93cc 45%,#7c7467 70%,#8a5535 100%)}
  .title__arc{position:absolute;left:330px;top:-30px}
  .title__mark{left:356px;top:66px;width:104px;height:104px;font-size:14px}
  .title__overline{position:absolute;left:24px;top:214px;font-size:20px;color:var(--ink-soft);letter-spacing:-.01em}
  .title__headline{position:absolute;left:24px;top:238px;font-size:44px;font-weight:700;letter-spacing:-.02em;white-space:nowrap}
  .title__rule-mid{position:absolute;left:24px;top:292px;width:138px;height:2px;background:var(--rule)}
  .title__sub{position:absolute;left:26px;top:306px;font-size:13px;color:var(--ink-soft)}

  /* content slides */
  .content__ring{position:absolute}
  .content__intro{font-size:6.5px;line-height:1.45;color:var(--ink-soft)}
  .content__heading{font-size:14px;font-weight:700;letter-spacing:-.02em;margin:14px 0 8px;color:#222}
  .content__body{font-size:6.5px;line-height:1.55;color:var(--ink-soft)}
  .content__rule{position:absolute;height:1px;background:var(--rule)}
  .content__footer{position:absolute;font-size:6px;color:var(--ink-soft)}

  .site__photo{left:0;top:0;width:238px;height:304px;background:linear-gradient(180deg,#3c74c9 0%,#8eb2e0 48%,#b8ab86 60%,#8c8a5e 80%,#6f6548 100%)}
  .site__text{position:absolute;left:266px;top:92px;width:240px}
  .site__rule{left:266px;top:270px;width:220px}
  .site__footer{left:430px;top:276px}
  .site__mark{left:498px;top:268px;width:20px;height:20px;font-size:3px}

  .facility__ghost{position:absolute;left:0;top:0}
  .facility__text{position:absolute;left:30px;top:94px;width:200px}
  .facility__photo{left:346px;top:0;width:194px;height:304px;background:linear-gradient(180deg,#6f8599 0%,#b39a86 38%,#d08a50 46%,#3b4652 62%,#1e262f 100%)}
  .facility__rule{left:30px;top:278px;width:300px}
  .facility__footer{left:465px;top:283px;color:#e8e8e8}
  .facility__mark{left:508px;top:276px;width:20px;height:20px;font-size:3px}
</style>
</head>
<body>

<section class="slide slide--title">
  <div class="title__rule-top"></div>
  <div class="photo title__photo" role="img" aria-label="Photograph of a drilling rig mast against a blue sky with stacked pipe and equipment in the foreground"></div>
  <svg class="title__arc" width="320" height="300" viewBox="0 0 320 300" aria-hidden="true">
    <path d="M30 30 A135 135 0 0 1 290 170 L250 170 A95 95 0 0 0 70 30 Z" fill="#5d5d5d" opacity=".85"/>
  </svg>
  <div class="mark title__mark">PELVORAN</div>
  <p class="title__overline">LOREM IPSUM</p>
  <h1 class="title__headline">LOREM IPSUM</h1>
  <div class="title__rule-mid"></div>
  <p class="title__sub">LOREM IPSUM</p>
</section>

<section class="slide slide--content slide--site">
  <div class="photo site__photo" role="img" aria-label="Photograph of a drilling rig on a dry grassland site under a clear blue sky"></div>
  <svg class="content__ring" style="left:330px;top:-40px" width="220" height="260" viewBox="0 0 220 260" aria-hidden="true">
    <circle cx="150" cy="110" r="115" fill="none" stroke="var(--ghost)" stroke-width="46"/>
  </svg>
  <div class="site__text">
    <p class="content__intro">Lorem ipsum dolor sit amet, consectetur adipiscing elit. Fusce id diam magna. Cras at orci egestas, tincidunt tortor vitae, viverra mi. Vestibulum in ipsum sapien.</p>
    <h2 class="content__heading">Lorem ipsum dolor sit amet.</h2>
    <p class="content__body">Lorem ipsum dolor sit amet, consectetur adipiscing elit. Fusce id diam magna. Cras at orci egestas, tincidunt tortor vitae, viverra mi. Vestibulum in ipsum sapien. Fusce in ipsum id augue ultricies consectetur. Sed et convallis lacus. Nam pretium est ac enim sagittis, quis placerat arcu faucibus. Nullam gravida lorem libero, vel sagittis felis interdum non. Proin et amet commodo libero.</p>
  </div>
  <div class="content__rule site__rule"></div>
  <p class="content__footer site__footer">Lorem ipsum | 01</p>
  <div class="mark site__mark">PELVORAN</div>
</section>

<section class="slide slide--content slide--facility">
  <svg class="facility__ghost" width="346" height="304" viewBox="0 0 346 304" aria-hidden="true">
    <path d="M0 0 H40 A70 70 0 0 1 40 110 H0 Z" fill="var(--ghost)"/>
    <rect x="265" y="0" width="81" height="304" fill="var(--ghost)"/>
    <rect x="100" y="150" width="175" height="154" fill="#f0f0f0"/>
  </svg>
  <div class="facility__text">
    <h2 class="content__heading" style="margin-top:0">Lorem ipsum dolor sit amet.</h2>
    <p class="content__body">Lorem ipsum dolor sit amet, consectetur adipiscing elit. Fusce id diam magna. Cras at orci egestas, tincidunt tortor vitae, viverra mi. Vestibulum in ipsum sapien. Fusce in ipsum id augue ultricies consectetur. Sed et convallis lacus. Nam pretium est ac enim sagittis, quis placerat arcu faucibus.</p>
  </div>
  <div class="photo facility__photo" role="img" aria-label="Photograph of a refinery's towers silhouetted against a dusk sky"></div>
  <div class="content__rule facility__rule"></div>
  <p class="content__footer facility__footer">Lorem ipsum | 01</p>
  <div class="mark facility__mark">PELVORAN</div>
</section>

</body>
</html>
```